Aesthetics Company Flyer (description of services)

We need a 5.5"x8.5" flyer describing the services we offer at velvet horizon aesthetics. We are an aesthetics company located in Conroe TX. Our products and services can be found at www.vhaesthetics-demo.com/services . We would like to see designs that are cohesive with our brand and website: https://www.vhaesthetics-demo.com/

```html
<!DOCTYPE html>
<html lang="en">
<head>
<meta charset="utf-8">
<title>Velvet Horizon Aesthetics – Services Flyer</title>
<link rel="stylesheet" href="https://fonts.googleapis.com/css2?family=Anton&family=Great+Vibes&family=Raleway:wght@300;400;500;800;900&family=Josefin+Sans:wght@700&display=swap">
<style>
  :root {
    --lilac: #cdb5f2;
    --lilac-soft: #e3d5fa;
    --lilac-pale: #f1eafc;
    --lilac-accent: #c3a6f0;
    --plum: #25143a;
    --ink: #2e2440;
    --white: #ffffff;
    --photo-dark: #2b2b2b;
  }
  * { box-sizing: border-box; margin: 0; padding: 0; }
  html, body { width: 845px; height: 1200px; overflow: hidden; background: var(--white); }
  .flyer { position: relative; width: 845px; height: 1200px; overflow: hidden; background: var(--white); font-family: "Raleway", sans-serif; color: var(--ink); }
  .backdrop { position: absolute; inset: 0; }

  .headline { position: absolute; left: 40px; top: 124px; font-family: "Anton", sans-serif; color: var(--plum); line-height: 1; font-weight: 400; }
  .headline-line { display: block; font-size: 82px; letter-spacing: -2px; white-space: nowrap; }
  .headline-line + .headline-line { margin-top: 10px; }
  .headline-script { font-family: "Great Vibes", cursive; color: var(--white); font-size: 92px; letter-spacing: 0; vertical-align: 10px; margin-left: 14px; }
  .headline-light { color: var(--white); }

  .brand { position: absolute; left: 500px; top: 92px; width: 300px; text-align: center; }
  .brand-disc { width: 150px; height: 150px; border-radius: 50%; background: var(--lilac-soft); margin: 0 auto 22px; }
  .brand-name { font-family: "Raleway", sans-serif; font-weight: 500; font-size: 14px; letter-spacing: 5px; color: var(--plum); }

  .services-title { position: absolute; left: 40px; top: 482px; font-family: "Raleway", sans-serif; font-weight: 900; font-size: 31px; line-height: 0.95; letter-spacing: -0.5px; }
  .services-title span { display: block; color: var(--plum); }
  .services-title .accent { color: var(--lilac-accent); }
  .services-copy { position: absolute; left: 40px; top: 564px; width: 380px; font-weight: 300; font-size: 16.5px; line-height: 21px; letter-spacing: -0.7px; color: #3a3446; }
  .services-copy p + p { margin-top: 12px; }

  .photo { position: absolute; left: 40px; top: 757px; width: 393px; height: 413px; border-radius: 8px; background: radial-gradient(ellipse at 55% 65%, #c99b7a 0%, #8c6248 28%, #3a312c 55%, var(--photo-dark) 80%); }

  .iv-badge { position: absolute; left: 498px; top: 479px; width: 286px; height: 56px; border-radius: 4px; background: var(--plum); color: var(--white); font-family: "Raleway", sans-serif; font-weight: 900; font-size: 30px; letter-spacing: -0.8px; display: flex; align-items: center; justify-content: center; }
  .iv-badge .accent { color: var(--lilac-accent); margin-right: 8px; }

  .iv-list { position: absolute; left: 498px; top: 552px; list-style: none; }
  .iv-item { display: flex; align-items: center; height: 26px; font-size: 23px; font-weight: 400; letter-spacing: -0.6px; color: var(--ink); position: absolute; left: 0; white-space: nowrap; }
  .iv-item svg { width: 18px; height: 16px; margin-right: 11px; flex: none; }
  .tick-light { stroke: var(--lilac-accent); }
  .tick-dark { stroke: var(--plum); }

  .contact { position: absolute; left: 498px; top: 967px; width: 303px; height: 203px; border-radius: 8px; background: var(--lilac); padding: 14px 16px; font-family: "Josefin Sans", sans-serif; font-weight: 700; color: var(--plum); }
  .contact-title { font-family: "Raleway", sans-serif; font-weight: 900; font-size: 29px; letter-spacing: -0.8px; line-height: 1; color: var(--plum); }
  .contact-title .accent { color: var(--white); }
  .contact-row { display: flex; align-items: flex-start; margin-top: 12px; font-size: 15px; line-height: 17px; }
  .contact-row svg { width: 16px; height: 16px; margin-right: 12px; flex: none; fill: var(--white); }
  .contact-row.phone { font-size: 17px; margin-top: 16px; }
  .contact-row.email { font-size: 14px; }
</style>
</head>
<body>
<main class="flyer">
  <svg class="backdrop" width="845" height="1200" viewBox="0 0 845 1200" aria-hidden="true">
    <path fill="var(--lilac-soft)" d="M0 0H845V588C780 592 720 540 662 488C612 444 522 428 462 488C405 540 350 520 318 470C270 390 235 340 190 346C140 352 110 460 40 462L0 466Z"/>
    <path fill="var(--lilac)" d="M0 0H845V572C780 578 720 522 660 470C610 430 520 410 455 470C400 518 360 500 330 450C285 375 235 318 190 326C145 334 118 440 60 445L0 445Z"/>
    <path fill="var(--lilac-pale)" d="M0 1200V1120C120 1100 260 1130 420 1200Z"/>
  </svg>
  <div role="img" aria-label="Soft leaf sprigs and botanical decoration" style="position:absolute;left:660px;top:320px;width:185px;height:180px;border-radius:50%;background:radial-gradient(circle,#6a4fa0 0%,rgba(160,130,220,0.5) 45%,rgba(205,181,242,0) 72%);"></div>
  <div role="img" aria-label="Botanical leaf decoration" style="position:absolute;left:0;top:1020px;width:120px;height:140px;border-radius:50%;background:radial-gradient(circle,#4a3570 0%,rgba(160,130,220,0.45) 45%,rgba(255,255,255,0) 72%);"></div>

  <h1 class="headline">
    <span class="headline-line">ONE<span class="headline-script">Beautiful</span></span>
    <span class="headline-line">FACE AT A <span class="headline-light">TIME</span></span>
  </h1>

  <div class="brand">
    <div class="brand-disc"></div>
    <p class="brand-name">VELVET HORIZON AESTHETICS</p>
  </div>

  <h2 class="services-title"><span>OUR</span><span class="accent">SERVICES</span></h2>
  <div class="services-copy">
    <p>At Velvet Horizon Aesthetics we offer a comprehensive list of aesthetic, skincare and weight loss services and IV hydration therapy.</p>
    <p>But before you embark on your journey with us, you must first book a consultation so we can assess and understand your needs and decide on the best option to address those needs.</p>
  </div>

  <div class="photo" role="img" aria-label="Portrait photograph of two smiling women with glowing skin on a dark backdrop"></div>

  <div class="iv-badge"><span class="accent">IV</span>HYDRATION</div>

  <ul class="iv-list">
    <li class="iv-item" style="top:1px"><svg viewBox="0 0 18 16"><path class="tick-light" d="M2 8l5 5L16 2" fill="none" stroke-width="3"/></svg>NAD+</li>
    <li class="iv-item" style="top:39px"><svg viewBox="0 0 18 16"><path class="tick-dark" d="M2 8l5 5L16 2" fill="none" stroke-width="3"/></svg>Quench&nbsp; Hydrator</li>
    <li class="iv-item" style="top:81px"><svg viewBox="0 0 18 16"><path class="tick-light" d="M2 8l5 5L16 2" fill="none" stroke-width="3"/></svg>Migraine Rescue</li>
    <li class="iv-item" style="top:123px"><svg viewBox="0 0 18 16"><path class="tick-dark" d="M2 8l5 5L16 2" fill="none" stroke-width="3"/></svg>Glutathione</li>
    <li class="iv-item" style="top:161px"><svg viewBox="0 0 18 16"><path class="tick-light" d="M2 8l5 5L16 2" fill="none" stroke-width="3"/></svg>Immunity Booster</li>
    <li class="iv-item" style="top:202px"><svg viewBox="0 0 18 16"><path class="tick-dark" d="M2 8l5 5L16 2" fill="none" stroke-width="3"/></svg>Myers’ Cocktail</li>
    <li class="iv-item" style="top:245px"><svg viewBox="0 0 18 16"><path class="tick-light" d="M2 8l5 5L16 2" fill="none" stroke-width="3"/></svg>Velvet Glow</li>
    <li class="iv-item" style="top:283px"><svg viewBox="0 0 18 16"><path class="tick-dark" d="M2 8l5 5L16 2" fill="none" stroke-width="3"/></svg>Hangover</li>
    <li class="iv-item" style="top:324px"><svg viewBox="0 0 18 16"><path class="tick-light" d="M2 8l5 5L16 2" fill="none" stroke-width="3"/></svg>Peak Athletic Performance</li>
    <li class="iv-item" style="top:362px"><svg viewBox="0 0 18 16"><path class="tick-dark" d="M2 8l5 5L16 2" fill="none" stroke-width="3"/></svg>Post Workout Recovery</li>
  </ul>

  <section class="contact">
    <h2 class="contact-title"><span class="accent">REACH</span> US!</h2>
    <p class="contact-row phone"><svg viewBox="0 0 24 24"><path d="M6.6 10.8a15.1 15.1 0 0 0 6.6 6.6l2.2-2.2a1 1 0 0 1 1-.25 11.4 11.4 0 0 0 3.6.57 1 1 0 0 1 1 1V20a1 1 0 0 1-1 1A17 17 0 0 1 3 4a1 1 0 0 1 1-1h3.5a1 1 0 0 1 1 1c0 1.25.2 2.450.57 3.57a1 1 0 0 1-.25 1z"/></svg>555 013 0198</p>
    <p class="contact-row email"><svg viewBox="0 0 24 24"><path d="M6 2l13 11h-6.5l3.5 7.5-2.5 1.2-3.5-7.6L6 19z"/></svg>hello@vhaesthetics-demo.com</p>
    <p class="contact-row"><svg viewBox="0 0 24 24"><path d="M12 2a7 7 0 0 0-7 7c0 5.2 7 13 7 13s7-7.8 7-13a7 7 0 0 0-7-7zm0 9.5A2.5 2.5 0 1 1 12 6.5a2.5 2.5 0 0 1 0 5z"/></svg><span>2150 Meadow Ridge Rd #300<br>Sampleton, TX 77000<br>(Across from Lumen Cinema)</span></p>
  </section>
</main>
</body>
</html>
```